Economic Book Cover

I need a book cover for a 5.5" x 8.5" paperback book that is 100 pages long. No title or words on the spine please, as the book is too thin to print on the spine. The title of the book is The Nine Harbor Lanterns. The subtitle is "The Patient Weave of Morning Light and Quiet Harbor Stones"
We'd like the cover to have a drawing of a dove offering an olive branch to a hundred dollar bill. You could use the attached illustration or create your own. The cover should be peaceful, hopeful, with cool colors.
The back cover should have the attached book description on it.
The authors name is Derek Halvorn and should be listed only on the front cover. No author's photo or description of the author need appear on the back cover, just the book description.
American voters

```html
<!DOCTYPE html>
<html lang="en">
<head>
<meta charset="utf-8">
<title>The Nine Harbor Lanterns — Cover Spread</title>
<link href="https://fonts.googleapis.com/css2?family=Bebas+Neue&family=EB+Garamond:ital@0;1&family=Libre+Caslon+Text:wght@700&family=Jost:wght@300&display=swap" rel="stylesheet">
<style>
  :root {
    --sky-top: #d9f0fb;
    --sky-mid: #5fb3e6;
    --sky-deep: #2a86cf;
    --horizon: #cfe9f8;
    --sea: #7fbde6;
    --title-red: #c91f28;
    --subtitle-blue: #1d5d8f;
    --ink: #111418;
    --badge-blue: #2a97d6;
    --note-grey: #a9a6a0;
  }
  * { margin: 0; padding: 0; box-sizing: border-box; }
  html, body { width: 1200px; height: 777px; overflow: hidden; background: #ffffff; }
  .cover-spread {
    position: relative;
    width: 1200px;
    height: 777px;
    overflow: hidden;
  }
  .backdrop {
    position: absolute; inset: 0;
    background:
      radial-gradient(ellipse 520px 260px at 880px 110px, rgba(255,255,255,0.9), rgba(255,255,255,0) 70%),
      radial-gradient(ellipse 700px 300px at 600px 330px, rgba(255,255,255,0.45), rgba(255,255,255,0) 70%),
      linear-gradient(180deg, var(--sky-top) 0%, var(--sky-mid) 30%, var(--sky-deep) 58%, var(--horizon) 80%, var(--sea) 100%);
  }
  /* Back cover */
  .back-cover {
    position: absolute;
    left: 32px; top: 86px;
    width: 513px;
    color: var(--ink);
    font-family: "EB Garamond", serif;
  }
  .back-title {
    font-style: italic;
    font-weight: 400;
    font-size: 30px;
    line-height: 34px;
  }
  .back-description p {
    font-size: 21px;
    line-height: 28.2px;
    text-align: justify;
    margin-bottom: 28px;
  }
  /* Front cover */
  .front-title {
    position: absolute;
    left: 646px; top: 22px;
    width: 508px;
    font-family: "Bebas Neue", sans-serif;
    color: var(--title-red);
    text-align: center;
    line-height: 0.88;
  }
  .front-title .line-one { display: block; font-size: 98px; letter-spacing: 2px; white-space: nowrap; }
  .front-title .numeral { font-size: 150px; vertical-align: -6px; }
  .front-title .line-two { display: block; font-size: 100px; letter-spacing: 4px; margin-top: 4px; }
  .subtitle {
    position: absolute;
    left: 648px; top: 250px;
    width: 506px;
    font-family: "Libre Caslon Text", serif;
    font-weight: 700;
    font-size: 20px;
    line-height: 30px;
    color: var(--subtitle-blue);
    text-align: center;
    text-transform: uppercase;
  }
  .emblem {
    position: absolute;
    left: 860px; top: 360px;
    width: 320px; height: 220px;
  }
  .author {
    position: absolute;
    left: 640px; top: 680px;
    width: 520px;
    text-align: center;
    font-family: "Jost", sans-serif;
    font-weight: 300;
    font-size: 70px;
    line-height: 80px;
    color: var(--ink);
    text-transform: uppercase;
    letter-spacing: -1px;
  }
</style>
</head>
<body>
<main class="cover-spread">
  <div class="backdrop" role="img" aria-label="Bright sky of soft clouds shaped like a world map above a calm blue sea"></div>

  <section class="back-cover">
    <h2 class="back-title">The Nine Harbor Lanterns</h2>
    <div class="back-description">
      <p>is a practical guide to the liberation of our nation’s economic woes. Halvorn introduces an entirely new way of looking at our economy that revolutionizes our financial system, producing an unprecedented level abundance for all.</p>
      <p>If we follow the Nine Harbor Lanterns, we can eliminate income taxes, balance our budget, and pay off the national debt. Our economy will boom, our citizens will prosper, and America will achieve a higher level of international prominence than ever before.</p>
    </div>
  </section>

  <h1 class="front-title">
    <span class="line-one">THE <span class="numeral">9</span> HARBOR</span>
    <span class="line-two">LANTERNS</span>
  </h1>

  <p class="subtitle">The Patient Weave of Morning Light<br>and Quiet Harbor Stones</p>

  <svg class="emblem" viewBox="0 0 320 220" xmlns="http://www.w3.org/2000/svg">
    <circle cx="212" cy="104" r="96" fill="var(--badge-blue)" role="img" aria-label="White dove carrying an olive branch"/>
    <rect x="14" y="118" width="180" height="88" fill="var(--note-grey)" stroke="#7d7a75" stroke-width="2" transform="rotate(4 104 162)" role="img" aria-label="Grey hundred dollar bill"/>
  </svg>

  <p class="author">Derek Halvorn</p>
</main>
</body>
</html>
```